Black Hair Stylist Business Card

Looking a for a business card for my hair styling business. Would like the card to be clean and giving our company a sophisticated look. I specialize in black hair styling including braids, sew ins and extensions. I have uploaded two versions of my logo, both are PNG files.

On the front of the card I would like my logo, name (Marisol Quenby), phone number (Will provide number to the winner, for now use a fake number) and the area I service which is Cedarholt, OR.

On the back I would like a list of the different styles of hair I do.
Knotless Braids - Feeding Braids - Bohemian Braids - Extensions - Sew In - Crochet - Butterfly Locs - Twist

On the back I would also like to note I have great reviews. Would be nice to have 5 Stars Emojis - TressNook I may also provide a QR code to take customers to my TressNook Page.

PLEASE NOTE: Originally I upload 2 versions of our logo. Now that we've seen some options we've decided to go with the pink logo and a white/cream white background.

Target Market(s)

Black Men and Women

Industry/Entity Type

Hair Styling and Design

Contact Information for Business Card

Please refer to the Project Description for details.

Font styles to use
Serif
Sans Serif

Colors
E54698
E96AAD
F1A4CE
F9D9EA
FCEFF6
A7469A
B969AE
D3A5CF
EDDBEB
F8F0F9

Requirements
Must have
• Please refer to the Project Description for details.
Nice to have
• Easy to read and feels sophisticated.
Should not have
• Should not be too busy looking.

```html
<!DOCTYPE html>
<html lang="en">
<head>
<meta charset="utf-8">
<title>Velora Braids &amp; Extensions – Business Card</title>
<link rel="stylesheet" href="https://fonts.googleapis.com/css2?family=Montserrat:wght@400;500;600&family=Gochi+Hand&display=swap">
<style>
  :root {
    --backdrop: #cfcfd0;
    --card: #ffffff;
    --pink: #e8198b;
    --purple: #a0429a;
    --white: #ffffff;
    --shadow: 0 4px 10px rgba(0, 0, 0, 0.28);
  }
  * { box-sizing: border-box; margin: 0; padding: 0; }
  html, body {
    width: 1200px;
    height: 1200px;
    overflow: hidden;
    background: var(--backdrop);
  }
  .sheet {
    position: relative;
    width: 1200px;
    height: 1200px;
  }
  .card {
    position: absolute;
    left: 160px;
    width: 880px;
    height: 516px;
    background: var(--card);
    box-shadow: var(--shadow);
    overflow: hidden;
  }
  .card--front { top: 56px; }
  .card--back { top: 622px; }

  .brand {
    position: absolute;
    display: flex;
    flex-direction: column;
    align-items: center;
    font-family: "Montserrat", sans-serif;
  }
  .brand__name {
    font-weight: 600;
    font-size: 104px;
    line-height: 1;
    color: var(--pink);
    letter-spacing: 1px;
  }
  .brand__tagline {
    margin-top: 44px;
    font-weight: 600;
    font-size: 19px;
    letter-spacing: 4px;
    color: var(--purple);
  }
  .card--front .brand { left: 70px; top: 80px; width: 340px; }
  .card--back .brand { left: 0; right: 0; top: 100px; }

  .owner {
    position: absolute;
    left: 58px;
    top: 388px;
    font-family: "Gochi Hand", cursive;
    font-size: 46px;
    line-height: 1;
    color: var(--purple);
    white-space: nowrap;
  }

  .accent-sweep {
    position: absolute;
    left: 0;
    top: 0;
    width: 880px;
    height: 516px;
  }

  .contact {
    position: absolute;
    right: 71px;
    top: 364px;
    list-style: none;
    font-family: "Montserrat", sans-serif;
    font-size: 21px;
    color: var(--white);
    text-align: right;
  }
  .contact__item {
    display: flex;
    align-items: center;
    justify-content: flex-end;
    gap: 18px;
    height: 34px;
  }
  .contact__icon { width: 15px; height: 15px; fill: var(--white); }

  .divider-band {
    position: absolute;
    left: 84px;
    top: 318px;
    width: 712px;
    height: 22px;
    border-radius: 11px;
    background: var(--purple);
  }

  .services {
    position: absolute;
    left: 0;
    right: 0;
    top: 392px;
    font-family: "Montserrat", sans-serif;
    font-weight: 500;
    font-size: 20px;
    line-height: 33px;
    color: var(--pink);
    text-align: center;
    text-transform: uppercase;
    letter-spacing: 0.3px;
  }
</style>
</head>
<body>
<main class="sheet">

  <section class="card card--front" aria-label="Business card front">
    <svg class="accent-sweep" viewBox="0 0 880 516" role="img" aria-label="Large pink wing-shaped sweep decoration">
      <path d="M455 516 C 400 440, 395 330, 470 285 C 540 245, 640 265, 720 262 C 790 260, 850 240, 880 232 L880 516 Z" fill="var(--pink)"/>
    </svg>

    <div class="brand">
      <span class="brand__name">Velora</span>
      <span class="brand__tagline">BRAIDS &amp; EXTENSIONS</span>
    </div>

    <p class="owner">Marisol Quenby</p>

    <ul class="contact">
      <li class="contact__item">
        <span>0402 555 0199</span>
        <svg class="contact__icon" viewBox="0 0 24 24" aria-hidden="true">
          <path d="M6.6 10.8a15.1 15.1 0 0 0 6.6 6.6l2.2-2.2a1 1 0 0 1 1-.25 11.4 11.4 0 0 0 3.6.57 1 1 0 0 1 1 1V20a1 1 0 0 1-1 1A17 17 0 0 1 3 4a1 1 0 0 1 1-1h3.5a1 1 0 0 1 1 1c0 1.25.2 2.45.57 3.57a1 1 0 0 1-.25 1z"/>
        </svg>
      </li>
      <li class="contact__item">
        <span>Cedarholt, OR</span>
        <svg class="contact__icon" viewBox="0 0 24 24" aria-hidden="true">
          <path d="M12 2a7 7 0 0 0-7 7c0 5.25 7 13 7 13s7-7.75 7-13a7 7 0 0 0-7-7zm0 9.5a2.5 2.5 0 1 1 0-5 2.5 2.5 0 0 1 0 5z"/>
        </svg>
      </li>
    </ul>
  </section>

  <section class="card card--back" aria-label="Business card back">
    <div class="brand">
      <span class="brand__name">Velora</span>
      <span class="brand__tagline">BRAIDS &amp; EXTENSIONS</span>
    </div>

    <div class="divider-band" role="img" aria-label="Purple interlaced ribbon flourish"></div>

    <p class="services">
      Knotless Braids - Feeding Braids - Bohemian Braids<br>
      Extensions - Sew In - Crochet - Butterfly Locs - Twist
    </p>
  </section>

</main>
</body>
</html>
```